Business Card Design

We have recently seen two business cards that caught our attention and think the designs would work for us. We are an accounting firm that serves small businesses in a variety of industries. Attached are the two business card that inspired us along with very rough layouts. We would like to see a professional layout using our company information.

Industry/Entity Type

Accounting

Contact Information for Business Card

Company Name - Porter Lyle
Address - 4120 Marbury Lane, Suite 310, Houston, TX 77058
713-555-0186 - Main
281-555-0143 - Fax

Team Member Names, emails and phone numbers (see attachment)

```html
<!DOCTYPE html>
<html lang="en">
<head>
<meta charset="utf-8">
<title>Porter Lyle – Business Card</title>
<link rel="stylesheet" href="https://fonts.googleapis.com/css2?family=Lato:wght@400;700;900&display=swap">
<style>
  :root {
    --backdrop: #2b2b2b;
    --card-light: #ffffff;
    --card-shade: #e4e4e4;
    --ink: #111111;
    --ink-soft: #8a8a8a;
    --rule-dark: #555555;
    --rule-light: #e6e6e6;
  }
  * { margin: 0; padding: 0; box-sizing: border-box; }
  html, body {
    width: 1200px; height: 900px; overflow: hidden;
    background: var(--backdrop);
    font-family: "Lato", Arial, sans-serif;
    color: var(--ink);
  }
  .card {
    position: absolute; left: 100px; top: 164px;
    width: 1000px; height: 572px;
    border-radius: 30px;
    background: linear-gradient(135deg, var(--card-light) 0%, #f6f6f6 55%, var(--card-shade) 100%);
  }
  .brand {
    position: absolute; left: 0; top: 120px; width: 880px;
    display: flex; align-items: center; justify-content: center; gap: 22px;
  }
  .brand-square { width: 44px; height: 44px; background: var(--ink); }
  .brand-name {
    font-weight: 900; font-size: 64px; letter-spacing: 1px;
    text-transform: uppercase; line-height: 1;
  }
  .divider {
    position: absolute; left: 500px; top: 268px; width: 4px; height: 210px;
    background: linear-gradient(to bottom, var(--rule-light), var(--rule-dark));
  }
  .person {
    position: absolute; right: 530px; top: 272px; text-align: right;
  }
  .person-name { font-weight: 900; font-size: 34px; text-transform: uppercase; line-height: 1.05; }
  .person-role { font-size: 20px; color: var(--ink-soft); margin-bottom: 14px; }
  .contact-line {
    display: flex; align-items: center; gap: 10px;
    font-size: 26px; line-height: 1.45;
  }
  .person .contact-line { justify-content: flex-end; }
  .icon { width: 24px; height: 24px; flex: none; }
  .email { position: absolute; left: 64px; top: 484px; }
  .office { position: absolute; left: 540px; top: 272px; }
  .address { font-size: 25px; line-height: 1.25; margin: 12px 0 14px; }
  .web { font-weight: 700; font-size: 24px; }
  .web-domain { color: var(--ink-soft); }
</style>
</head>
<body>
  <section class="card" aria-label="Porter Lyle business card">
    <div class="brand">
      <span class="brand-square" aria-hidden="true"></span>
      <span class="brand-name">Porter Lyle</span>
    </div>

    <div class="person">
      <p class="person-name">Marisol Dunne</p>
      <p class="person-role">Account Manager</p>
      <p class="contact-line">
        <svg class="icon" viewBox="0 0 24 24" aria-hidden="true"><path d="M3 9c0-3 4-5 9-5s9 2 9 5l-4 1-1-3H8L7 10z M6 12h12l2 8H4z" fill="currentColor"/></svg>
        713-555-0186
      </p>
      <p class="contact-line">
        <svg class="icon" viewBox="0 0 24 24" aria-hidden="true"><rect x="6" y="2" width="12" height="20" rx="2" fill="none" stroke="currentColor" stroke-width="2"/></svg>
        832-555-0172
      </p>
    </div>

    <p class="contact-line email">
      <svg class="icon" viewBox="0 0 24 24" aria-hidden="true"><rect x="2" y="5" width="20" height="14" fill="currentColor"/><path d="M2 5l10 8 10-8" fill="none" stroke="#fff" stroke-width="1.6"/></svg>
      mdunne@porterlyle.com
    </p>

    <div class="divider" aria-hidden="true"></div>

    <div class="office">
      <p class="contact-line">
        <svg class="icon" viewBox="0 0 24 24" aria-hidden="true"><path d="M3 9c0-3 4-5 9-5s9 2 9 5l-4 1-1-3H8L7 10z M6 12h12l2 8H4z" fill="currentColor"/></svg>
        713-555-0186
      </p>
      <p class="contact-line">
        <svg class="icon" viewBox="0 0 24 24" aria-hidden="true"><rect x="7" y="3" width="10" height="6" fill="currentColor"/><rect x="2" y="9" width="20" height="9" rx="2" fill="currentColor"/><rect x="6" y="15" width="12" height="6" fill="#fff" stroke="currentColor" stroke-width="2"/></svg>
        281-555-0143
      </p>
      <p class="address">4120 Marbury Lane, Suite 310,<br>Houston, TX 77058</p>
      <p class="web">www.<span class="web-domain">porterlyle</span>.com</p>
    </div>
  </section>
</body>
</html>
```